TRELLWICK Construction Group business card for distribution

A business card detailing our services, with our phone number and email address.
- Groundworks / Foundations / Drainage
- Landscaping / Hard Landscaping / Patios / Decking
- Fencing
The card should include company logo and be in the same colours.

Target Market(s)
Domestic Houses
Industry/Entity Type
Construction
Contact Information for Business Card
Phone Number - 07931 258 904 / 07713829516. Email address: trellgroup@stonevane-mail.com
Font styles to use
Serif
Sans Serif
Colors
F0912C
F2A743
F7CA91
FBE8D2
FDF5EE
Requirements
Must have
- Contact numbers. Photos of past work. Company Logo

Nice to have
- Company Logo

```html
<!DOCTYPE html>
<html lang="en">
<head>
<meta charset="utf-8">
<title>TRELLWICK Construction Group – Business Card</title>
<link href="https://fonts.googleapis.com/css2?family=Montserrat:wght@700&family=Roboto:wght@400&family=Roboto+Condensed:wght@700&display=swap" rel="stylesheet">
<style>
  :root {
    --backdrop: #9a9a9a;
    --card-black: #231f20;
    --card-white: #ffffff;
    --stone-grey: #bcbec0;
    --accent-orange: #f0912c;
    --ink-white: #ffffff;
    --ink-dark: #231f20;
  }
  html, body {
    margin: 0;
    width: 1200px;
    height: 1015px;
    overflow: hidden;
    background: radial-gradient(ellipse at 40% 45%, #b3b3b3 0%, var(--backdrop) 60%, #7d7d7d 100%);
  }
  .card {
    position: absolute;
    left: 220px;
    width: 760px;
    height: 434px;
    box-shadow: 0 14px 30px rgba(0,0,0,0.45);
    overflow: hidden;
  }
  .card--front { top: 44px; background: var(--card-black); }
  .card--back { top: 521px; background: var(--card-white); }

  .brand {
    position: absolute;
    left: 0; right: 0;
    display: flex;
    flex-direction: column;
    align-items: center;
    font-family: "Montserrat", sans-serif;
    font-weight: 700;
  }
  .brand__row { display: flex; align-items: center; gap: 14px; }
  .brand__mark { width: 34px; height: 34px; background: var(--accent-orange); }
  .brand__name { font-size: 58px; letter-spacing: 2px; line-height: 1; }
  .brand__sub { font-size: 19px; letter-spacing: 4px; margin-top: 12px; text-transform: uppercase; }

  .card--front .brand { top: 150px; color: var(--ink-white); }
  .card--back .brand { top: 26px; color: var(--ink-dark); }
  .card--back .brand__name { font-size: 50px; }
  .card--back .brand__sub { font-size: 17px; margin-top: 10px; }

  .terrain { position: absolute; inset: 0; width: 760px; height: 434px; }
  .terrain__band { fill: var(--card-black); }
  .terrain__base { fill: var(--stone-grey); }

  .services {
    position: absolute;
    left: 0; right: 0;
    top: 212px;
    text-align: center;
    font-family: "Roboto", sans-serif;
    font-size: 19px;
    line-height: 1.35;
    color: var(--ink-white);
  }
  .services .sep { color: var(--accent-orange); padding: 0 6px; }

  .contact {
    position: absolute;
    display: flex;
    align-items: center;
    gap: 8px;
    font-family: "Roboto Condensed", sans-serif;
    font-weight: 700;
    font-size: 21px;
    color: var(--ink-dark);
  }
  .contact .sep { color: var(--accent-orange); padding: 0 4px; font-weight: 400; }
  .contact--phone { left: 28px; top: 388px; }
  .contact--email { right: 24px; top: 328px; }
  .contact__icon { width: 26px; height: 26px; flex: none; }
</style>
</head>
<body>

<section class="card card--front" aria-label="Business card front">
  <div class="brand">
    <div class="brand__row">
      <span class="brand__mark"></span>
      <span class="brand__name">TRELLWICK</span>
    </div>
    <span class="brand__sub">Construction Group Ltd</span>
  </div>
</section>

<section class="card card--back" aria-label="Business card back">
  <svg class="terrain" viewBox="0 0 760 434" aria-hidden="true">
    <polygon class="terrain__band" points="0,255 60,244 110,214 170,204 230,190 300,180 360,172 420,166 480,152 540,142 600,128 650,106 700,90 760,98 760,434 0,434"/>
    <polygon class="terrain__base" points="0,345 40,336 62,308 120,302 200,306 260,304 320,308 380,306 440,298 500,284 560,262 620,244 680,220 720,198 760,204 760,434 0,434"/>
  </svg>

  <div class="brand">
    <div class="brand__row">
      <span class="brand__mark"></span>
      <span class="brand__name">TRELLWICK</span>
    </div>
    <span class="brand__sub">Construction Group Ltd</span>
  </div>

  <div class="services">
    Groundworks<span class="sep">|</span>Foundations<span class="sep">|</span>Drainage<br>
    Landscaping<span class="sep">|</span>Hard Landscaping<span class="sep">|</span>Patios<span class="sep">|</span>Decking<br>
    Fencing
  </div>

  <div class="contact contact--phone">
    <svg class="contact__icon" viewBox="0 0 26 26" aria-hidden="true">
      <circle cx="13" cy="13" r="13" fill="#f0912c"/>
      <path d="M9 7.5c.6-.4 1.3-.3 1.7.3l1.2 1.8c.3.5.2 1.1-.2 1.5l-.8.7c.6 1.3 1.6 2.4 2.9 3l.7-.8c.4-.4 1-.5 1.5-.2l1.8 1.2c.6.4.7 1.1.3 1.7l-.6.8c-.6.8-1.7 1.1-2.6.7-3-1.3-5.3-3.700-6.600-6.600-.4-.9-.1-2 .7-2.600z" fill="#231f20"/>
    </svg>
    <span>07931 258 904<span class="sep">|</span>07713829516</span>
  </div>

  <div class="contact contact--email">
    <span>trellgroup@stonevane-mail.com</span>
    <svg class="contact__icon" viewBox="0 0 26 26" aria-hidden="true">
      <circle cx="13" cy="13" r="13" fill="#f0912c"/>
      <rect x="7" y="9" width="12" height="8" fill="#231f20"/>
      <path d="M7 9l6 5 6-5" fill="none" stroke="#f0912c" stroke-width="1.2"/>
    </svg>
  </div>
</section>

</body>
</html>
```